Manufacturing company needs new business card.

I need a unique Business Card that will truly stand out. Nothing too busy. Simple is good, right? Not looking for a standard design either. No cookie cutter layout. I am just looking for something interesting and a bit different. Does't have to completely off the wall crazy, just not your run of the mill business card. Clean and modern with a touch of industrial.

Target Market(s)

Air conditioning industry, Architects, builders.

Industry/Entity Type

Business

Contact Information for Business Card

Details to be included on card are:

Peter Vance
Managing Director

T: 1300 847 519
M: 0428 593 174
W: www.brenvaleworks.com.au
E: peter.vance@brenvaleworks.com.au
A: 58 Harwick Lane, Sydney NSW 2000

Font styles to use
Sans Serif

Colors
0355a3
848484
fbfbfb

Requirements
Must have
• Card design must be landscape.

```html
<!DOCTYPE html>
<html lang="en">
<head>
<meta charset="utf-8">
<title>Brenvale Works – Business Card</title>
<link rel="stylesheet" href="https://fonts.googleapis.com/css2?family=Saira+Semi+Condensed:wght@400;600;700&family=Saira+Condensed:wght@400&family=Roboto:wght@400&display=swap">
<style>
  :root {
    --brand-blue: #313f87;
    --brand-grey: #6f7173;
    --card-white: #fbfbfb;
    --text-grey: #5a5c5f;
    --backdrop: #a9a7a8;
  }
  html, body {
    margin: 0;
    width: 1200px;
    height: 1200px;
    overflow: hidden;
    background: var(--backdrop);
  }
  .canvas {
    position: relative;
    width: 1200px;
    height: 1200px;
  }
  .card {
    position: absolute;
    width: 713px;
    height: 420px;
  }
  .card--front {
    left: 238px;
    top: 117px;
    background: var(--brand-blue);
  }
  .card--back {
    left: 230px;
    top: 644px;
    height: 417px;
    background: var(--card-white);
  }
  .lockup {
    position: absolute;
    left: 90px;
    top: 173px;
    display: flex;
    align-items: center;
    gap: 34px;
  }
  .lockup__square {
    width: 76px;
    height: 76px;
    background: var(--card-white);
    border-radius: 5px;
  }
  .lockup__name {
    font-family: "Saira Semi Condensed", sans-serif;
    font-weight: 600;
    font-size: 46px;
    color: var(--card-white);
    letter-spacing: 0.2px;
    line-height: 1;
  }
  .back__square {
    position: absolute;
    left: 87px;
    top: 116px;
    width: 189px;
    height: 184px;
    background: var(--brand-blue);
    border-radius: 10px;
  }
  .person {
    position: absolute;
    left: 368px;
    top: 110px;
  }
  .person__name {
    margin: 0;
    font-family: "Saira Semi Condensed", sans-serif;
    font-weight: 700;
    font-size: 29px;
    line-height: 1;
    color: var(--brand-blue);
  }
  .person__role {
    margin: 8px 0 0;
    font-family: "Roboto", sans-serif;
    font-size: 15px;
    color: var(--text-grey);
  }
  .contacts {
    list-style: none;
    margin: 0;
    padding: 0;
    position: absolute;
    left: 366px;
    top: 187px;
  }
  .contacts__item {
    display: flex;
    align-items: center;
    height: 23.3px;
    font-family: "Saira Condensed", sans-serif;
    font-size: 15.5px;
    color: var(--text-grey);
  }
  .contacts__icon {
    width: 18px;
    height: 16px;
    margin-right: 18px;
    fill: var(--brand-blue);
    flex: none;
  }
</style>
</head>
<body>
<main class="canvas">
  <section class="card card--front" aria-label="Card front">
    <div class="lockup">
      <div class="lockup__square"></div>
      <span class="lockup__name">Brenvale Works</span>
    </div>
  </section>

  <section class="card card--back" aria-label="Card back">
    <div class="back__square"></div>
    <div class="person">
      <h1 class="person__name">Peter Vance</h1>
      <p class="person__role">Managing Director</p>
    </div>
    <ul class="contacts">
      <li class="contacts__item">
        <svg class="contacts__icon" viewBox="0 0 18 16"><path d="M1 5c0-2 3-3 8-3s8 1 8 3v1.5h-4V5H5v1.5H1z"/><path d="M4 8h10l2 6H2z"/></svg>
        1300 847 519
      </li>
      <li class="contacts__item">
        <svg class="contacts__icon" viewBox="0 0 18 16"><path d="M5.5 0h7a1 1 0 0 1 1 1v14a1 1 0 0 1-1 1h-7a1 1 0 0 1-1-1V1a1 1 0 0 1 1-1zm1 2v10h5V2z"/></svg>
        0428 593 174
      </li>
      <li class="contacts__item">
        <svg class="contacts__icon" viewBox="0 0 18 16"><path d="M9 1a7 7 0 1 0 0 14A7 7 0 0 0 9 1zm0 1.4c.8 0 1.7 1.8 2 4.6H7c.3-2.8 1.2-4.6 2-4.6zM3.5 7h2.2c.1-1.8.5-3.3 1.1-4.2A5.7 5.7 0 0 0 3.5 7zm8.8 0h2.2a5.7 5.7 0 0 0-3.3-4.2c.6.9 1 2.4 1.1 4.2zM3.5 9a5.7 5.7 0 0 0 3.3 4.2c-.6-.9-1-2.4-1.1-4.2zm3.5 0c.3 2.8 1.2 4.6 2 4.6s1.7-1.8 2-4.6zm5.3 0c-.1 1.8-.5 3.3-1.1 4.2A5.7 5.7 0 0 0 14.5 9z"/></svg>
        www.brenvaleworks.com.au
      </li>
      <li class="contacts__item">
        <svg class="contacts__icon" viewBox="0 0 18 16"><path d="M0 3h18v10H0zm2 1.5 7 5 7-5v-.2H2zM1.5 12h15L11 8l-2 1.5L7 8z"/></svg>
        peter.vance@brenvaleworks.com.au
      </li>
      <li class="contacts__item">
        <svg class="contacts__icon" viewBox="0 0 18 16"><path d="M9 0a5.5 5.5 0 0 0-5.5 5.5C3.5 10 9 16 9 16s5.5-6 5.5-10.5A5.5 5.5 0 0 0 9 0zm0 3.2a2.3 2.3 0 1 1 0 4.6 2.3 2.3 0 0 1 0-4.6z"/></svg>
        58 Harwick Lane, Sydney NSW 2000
      </li>
    </ul>
  </section>
</main>
</body>
</html>
```